Modern Business Card

Modern professional business card with more than just logo and demographic info. Something memorable.

We are a trendy/modern chiropractic group with an emphasis on neurology, hence the minimalist-type brain logo. We want to convey that modern and technical aspect with professionalism and the elite nature of our practice environment.

```html
<!DOCTYPE html>
<html lang="en">
<head>
<meta charset="utf-8">
<title>Cortexa Spine — Business Card</title>
<link rel="stylesheet" href="https://fonts.googleapis.com/css2?family=Open+Sans:wght@400;600;700&display=swap">
<style>
  :root {
    --backdrop: #2b2b2e;
    --card-black: #121214;
    --card-charcoal: #1c1c1f;
    --brand-blue: #4a79c6;
    --brand-blue-deep: #3a64ab;
    --divider-grey: #8a8d94;
    --ink-white: #ffffff;
    --ink-soft: #e8eef8;
    --emboss: #2a2a2e;
  }
  * { box-sizing: border-box; margin: 0; padding: 0; }
  html, body { width: 800px; height: 1200px; overflow: hidden; }
  body {
    background: var(--backdrop);
    font-family: "Open Sans", Arial, sans-serif;
    position: relative;
  }
  .card {
    position: absolute;
    left: 90px;
    width: 620px;
    height: 355px;
    border-radius: 4px;
    overflow: hidden;
  }
  .card-front {
    top: 150px;
    background: var(--card-black);
    display: flex;
    align-items: center;
    justify-content: center;
  }
  .front-mark {
    display: flex;
    align-items: center;
    gap: 18px;
    color: var(--emboss);
    font-weight: 700;
    font-size: 46px;
    letter-spacing: 2px;
  }
  .front-mark .mark-square {
    width: 38px; height: 38px;
    background: var(--emboss);
  }
  .card-back { top: 695px; background: var(--card-charcoal); }
  .card-back svg.back-shape { position: absolute; inset: 0; }
  .brand {
    position: absolute;
    left: 48px; top: 150px;
    display: flex; align-items: center; gap: 10px;
    color: var(--ink-white);
    font-weight: 600;
    font-size: 24px;
    letter-spacing: 1px;
  }
  .brand .brand-square { width: 22px; height: 22px; background: var(--brand-blue); }
  .contact {
    position: absolute;
    left: 345px; top: 62px;
    color: var(--ink-white);
  }
  .contact-name { font-size: 20px; font-weight: 700; }
  .contact-title { font-size: 11px; color: var(--ink-soft); margin-top: 2px; margin-bottom: 20px; }
  .contact-list { list-style: none; font-size: 11px; color: var(--ink-soft); }
  .contact-list li { display: flex; align-items: flex-start; gap: 10px; margin-bottom: 9px; line-height: 1.4; }
  .contact-list svg { width: 13px; height: 13px; flex: none; margin-top: 1px; }
</style>
</head>
<body>
  <section class="card card-front" aria-label="Card front">
    <div class="front-mark"><span class="mark-square"></span>CORTEXA SPINE</div>
  </section>

  <section class="card card-back" aria-label="Card back">
    <svg class="back-shape" width="620" height="355" viewBox="0 0 620 355">
      <path d="M292 0 C235 90 225 260 268 355" fill="none" stroke="var(--divider-grey)" stroke-width="5"/>
      <path d="M300 0 H620 V355 H276 C233 260 243 90 300 0 Z" fill="var(--brand-blue)"/>
    </svg>
    <div class="brand"><span class="brand-square"></span>CORTEXA SPINE</div>
    <div class="contact">
      <div class="contact-name">Evan Marlow</div>
      <div class="contact-title">Managing Director</div>
      <ul class="contact-list">
        <li><svg viewBox="0 0 16 16"><path d="M4 1h3l1 4-2 1a9 9 0 0 0 4 4l1-2 4 1v3a2 2 0 0 1-2 2A13 13 0 0 1 2 3a2 2 0 0 1 2-2z" fill="#fff"/></svg>555.014.2270</li>
        <li><svg viewBox="0 0 16 16"><rect x="1" y="3" width="14" height="10" rx="1" fill="none" stroke="#fff" stroke-width="1.5"/><path d="M1.5 4l6.5 5 6.5-5" fill="none" stroke="#fff" stroke-width="1.5"/></svg>evan@cortexaspine.com</li>
        <li><svg viewBox="0 0 16 16"><circle cx="8" cy="8" r="6.5" fill="none" stroke="#fff" stroke-width="1.4"/><path d="M1.5 8h13M8 1.5c-3 3.5-3 9.5 0 13M8 1.5c3 3.5 3 9.5 0 13" fill="none" stroke="#fff" stroke-width="1.2"/></svg>www.cortexaspine.com</li>
        <li><svg viewBox="0 0 16 16"><path d="M8 15s5-5.5 5-9A5 5 0 0 0 3 6c0 3.5 5 9 5 9z" fill="#fff"/><circle cx="8" cy="6" r="1.8" fill="var(--brand-blue)"/></svg><span>48 Meridian Ave., Lakeview<br>Northvale, US 10482</span></li>
      </ul>
    </div>
  </section>
</body>
</html>
```